New business card/stationary for a consulting company

I am looking for a clean and very professional looking business card for my consulting company as well as corresponding stationary. I am uploading our logo. I like simple and powerful for the feel. No graphics but I am open on everything else. Below is my contact information but would like the final to be in a version I can add my employees information into and print. Thank you.

Daniel Whitcombe
dan@fernlowadvisory.com
2837 North 9th Avenue, Summit Floor, Larkmoor, Westvale 60483
www.fernlowadvisory.com

Industry/Entity Type

Consulting

Contact Information for Business Card

Daniel Whitcombe
dan@fernlowadvisory.com
www.fernlowadvisory.com

Font styles to use
Serif
Sans Serif

Requirements
Must have
• Our logo and the business card details.
Nice to have
• our website www.fernlowadvisory.com

```html
<!DOCTYPE html>
<html lang="en">
<head>
<meta charset="utf-8">
<title>Fernlow Advisory — Business Card</title>
<link href="https://fonts.googleapis.com/css2?family=Questrial&family=Crimson+Pro:ital,wght@0,400;0,700;1,400&display=swap" rel="stylesheet">
<style>
  :root {
    --navy: #0a0fa3;
    --navy-deep: #050a6e;
    --paper: #f4f4f4;
    --ink: #1a1a1a;
    --rule: #3a3a3a;
    --backdrop: #2a2a2c;
    --white: #ffffff;
  }
  * { box-sizing: border-box; margin: 0; padding: 0; }
  html, body { width: 1200px; height: 900px; overflow: hidden; }
  body {
    background: var(--backdrop);
    display: flex;
    flex-direction: column;
    align-items: center;
    justify-content: center;
    gap: 30px;
  }
  .card {
    position: relative;
    width: 700px;
    height: 400px;
    overflow: hidden;
    box-shadow: 0 10px 30px rgba(0,0,0,.45);
  }

  /* Front */
  .card-front { background: var(--paper); }
  .front-brand {
    position: absolute;
    left: 210px;
    top: 70px;
    display: flex;
    align-items: center;
    gap: 14px;
  }
  .brand-mark {
    width: 34px;
    height: 34px;
    background: var(--navy);
  }
  .brand-name {
    font-family: "Questrial", sans-serif;
    font-size: 30px;
    letter-spacing: 1px;
    color: var(--navy);
    text-transform: uppercase;
    white-space: nowrap;
  }
  .front-rule {
    position: absolute;
    left: 0;
    top: 196px;
    width: 405px;
    height: 1.5px;
    background: var(--rule);
  }
  .holder-name {
    position: absolute;
    left: 412px;
    top: 182px;
    font-family: "Crimson Pro", serif;
    font-weight: 700;
    font-size: 27px;
    letter-spacing: .5px;
    color: var(--navy);
    text-transform: uppercase;
    white-space: nowrap;
  }
  .contact-list {
    position: absolute;
    left: 40px;
    top: 222px;
    list-style: none;
    display: flex;
    flex-direction: column;
    gap: 8px;
  }
  .contact-item, .address {
    display: flex;
    align-items: flex-start;
    gap: 10px;
    font-family: "Crimson Pro", serif;
    font-size: 16px;
    color: var(--ink);
    line-height: 1.25;
  }
  .icon-chip {
    flex: none;
    width: 20px;
    height: 20px;
    background: var(--navy);
    display: flex;
    align-items: center;
    justify-content: center;
  }
  .address {
    position: absolute;
    left: 330px;
    top: 232px;
  }
  .address .icon-chip { margin-top: 1px; }
  .front-band {
    position: absolute;
    left: 0;
    bottom: 0;
    width: 100%;
    height: 34px;
    background: var(--navy);
  }

  /* Back */
  .card-back {
    background: radial-gradient(ellipse at 40% 40%, var(--navy) 0%, var(--navy-deep) 100%);
  }
  .back-brand {
    position: absolute;
    left: 0;
    right: 0;
    top: 120px;
    display: flex;
    align-items: center;
    justify-content: center;
    gap: 16px;
  }
  .back-brand .brand-mark { background: var(--white); width: 40px; height: 40px; }
  .back-brand .brand-name { color: var(--white); font-size: 40px; }
  .back-web {
    position: absolute;
    left: 0;
    right: 0;
    top: 205px;
    text-align: center;
    font-family: "Crimson Pro", serif;
    font-size: 20px;
    color: var(--white);
    letter-spacing: .5px;
  }
  .back-rule {
    position: absolute;
    height: 2px;
    background: var(--white);
  }
  .back-rule.left { left: 0; top: 330px; width: 200px; }
  .back-rule.right { right: 0; top: 270px; width: 200px; }
</style>
</head>
<body>

<section class="card card-front">
  <div class="front-brand">
    <div class="brand-mark"></div>
    <div class="brand-name">Fernlow Advisory</div>
  </div>

  <div class="front-rule"></div>
  <h1 class="holder-name">Daniel Whitcombe</h1>

  <ul class="contact-list">
    <li class="contact-item">
      <span class="icon-chip">
        <svg width="12" height="10" viewBox="0 0 12 10"><rect x="0.75" y="0.75" width="10.5" height="8.5" fill="none" stroke="#fff" stroke-width="1.3"/><path d="M1 1.2 L6 5.5 L11 1.2" fill="none" stroke="#fff" stroke-width="1.3"/></svg>
      </span>
      dan@fernlowadvisory.com
    </li>
    <li class="contact-item">
      <span class="icon-chip">
        <svg width="12" height="12" viewBox="0 0 12 12"><circle cx="6" cy="6" r="5" fill="none" stroke="#fff" stroke-width="1.3"/><path d="M1 6 H11 M6 1 C3.5 3.5 3.5 8.5 6 11 M6 1 C8.5 3.5 8.5 8.5 6 11" fill="none" stroke="#fff" stroke-width="1"/></svg>
      </span>
      www.fernlowadvisory.com
    </li>
  </ul>

  <div class="address">
    <span class="icon-chip">
      <svg width="10" height="13" viewBox="0 0 10 13"><path d="M5 12.5 C2 8.5 0.7 6.5 0.7 4.7 A4.3 4.3 0 0 1 9.3 4.7 C9.3 6.5 8 8.5 5 12.5 Z" fill="#fff"/><circle cx="5" cy="4.7" r="1.6" fill="#0a0fa3"/></svg>
    </span>
    <span>2837 North 9th Avenue, Summit Floor,<br>Larkmoor, Westvale 60483</span>
  </div>

  <div class="front-band"></div>
</section>

<section class="card card-back">
  <div class="back-brand">
    <div class="brand-mark"></div>
    <div class="brand-name">Fernlow Advisory</div>
  </div>
  <p class="back-web">www.fernlowadvisory.com</p>
  <div class="back-rule right"></div>
  <div class="back-rule left"></div>
</section>

</body>
</html>
```